Couples Workshop Flyer

I need a flyer to promote a one-day workshop for couples.

I am a therapist and life-coach and the session is called: "Lantern Pairs Rising, and bring out the best in each other' - so Lantern Pairs Rising is the bold name for the seminar but the point of the whole workshop is in the tagline, 'and bring out the best in each other'.

The final design should compel couples to take the risk to leave their comfort zones and attend a one-day workshop on a weekend .

Target Market(s)

Couples who are interested in self-improvement and identify with change and growth.
Somehow the flyer will match their aspirations!

Requirements
Should not have
• Not too many love hearts! :)
Not too gushy - a hint of romance!

```html
<!DOCTYPE html>
<html lang="en">
<head>
<meta charset="utf-8">
<title>Lantern Pairs Rising – One-Day Couples Seminar</title>
<link href="https://fonts.googleapis.com/css2?family=Roboto+Condensed:wght@300;400;700;900&family=Open+Sans:wght@400;600;700&display=swap" rel="stylesheet">
<style>
  :root {
    --brand-blue: #1b8fd9;
    --band-blue: #1a9ad6;
    --text-grey: #555a5f;
    --body-dark: #3a3d40;
    --url-grey: #6b6f73;
    --white: #ffffff;
    --sky-top: #eaf4fb;
    --sky-mid: #cfe5f3;
    --sea: #9cc9e6;
    --sand: #f3f1ec;
  }
  * { box-sizing: border-box; margin: 0; padding: 0; }
  html, body { width: 849px; height: 1200px; overflow: hidden; background: var(--white); }
  .flyer {
    position: relative;
    width: 849px;
    height: 1200px;
    overflow: hidden;
    background: var(--white);
    font-family: "Open Sans", Arial, sans-serif;
  }
  .site-url {
    position: absolute;
    top: 34px;
    right: 53px;
    font-weight: 700;
    font-size: 19px;
    color: var(--url-grey);
  }
  .hero-photo {
    position: absolute;
    left: 330px;
    top: 300px;
    width: 519px;
    height: 638px;
    background:
      radial-gradient(ellipse at 60% 55%, rgba(255,255,255,0.9) 0%, rgba(255,255,255,0) 45%),
      linear-gradient(180deg, var(--sky-top) 0%, var(--sky-mid) 35%, var(--sea) 60%, var(--sand) 100%);
    -webkit-mask-image: linear-gradient(90deg, transparent 0%, #000 22%);
    mask-image: linear-gradient(90deg, transparent 0%, #000 22%);
  }
  .title {
    position: absolute;
    left: 66px;
    top: 94px;
    font-family: "Roboto Condensed", "Arial Narrow", sans-serif;
    font-weight: 900;
    font-size: 68px;
    line-height: 1;
    letter-spacing: 0.5px;
    color: var(--brand-blue);
    text-transform: uppercase;
  }
  .tagline {
    position: absolute;
    left: 66px;
    top: 164px;
    font-family: "Roboto Condensed", "Arial Narrow", sans-serif;
    font-weight: 300;
    font-size: 40px;
    line-height: 1.1;
    color: var(--brand-blue);
  }
  .intro {
    position: absolute;
    left: 66px;
    top: 216px;
    width: 740px;
    font-size: 15.5px;
    line-height: 26px;
    color: var(--text-grey);
  }
  .intro p + p { margin-top: 3px; }
  .gains {
    position: absolute;
    left: 68px;
    top: 326px;
    width: 352px;
  }
  .gains-heading {
    font-weight: 700;
    font-size: 20.5px;
    line-height: 1.35;
    color: var(--brand-blue);
    margin-bottom: 24px;
  }
  .gains-list { list-style: none; }
  .gains-list li {
    position: relative;
    padding-left: 23px;
    font-size: 14.4px;
    line-height: 19.5px;
    color: var(--body-dark);
    margin-bottom: 5px;
  }
  .gains-list li svg {
    position: absolute;
    left: 0;
    top: 3px;
    width: 13px;
    height: 13px;
  }
  .presenter-band {
    position: absolute;
    left: 0;
    top: 936px;
    width: 849px;
    height: 264px;
    background: var(--band-blue);
    color: var(--white);
  }
  .presenter-photo {
    position: absolute;
    left: 36px;
    top: 40px;
    width: 120px;
    height: 184px;
    border: 2px solid var(--white);
    background: linear-gradient(180deg, #a9c98a 0%, #7fa766 45%, #d8c3ae 75%, #e8e4de 100%);
  }
  .presenter-text {
    position: absolute;
    left: 188px;
    top: 34px;
    width: 630px;
  }
  .presenter-heading {
    font-weight: 700;
    font-size: 18.5px;
    line-height: 24px;
    letter-spacing: 0.3px;
    margin-bottom: 2px;
  }
  .presenter-text p {
    font-size: 14.2px;
    line-height: 20px;
    margin-bottom: 5px;
  }
  .presenter-text .booking { margin-bottom: 0; margin-top: 8px; }
  .booking-url {
    display: block;
    font-weight: 700;
    font-size: 17px;
    line-height: 20px;
  }
</style>
</head>
<body>
<div class="flyer">
  <div class="site-url">declanmarlowe.com.au</div>

  <div class="hero-photo" role="img" aria-label="Smiling bride and groom embracing on a sunny beach, bride holding a white bouquet"></div>

  <h1 class="title">Lantern Pairs Rising</h1>
  <h2 class="tagline">and bring out the best in each other</h2>

  <div class="intro">
    <p>Some couples spend up big on their wedding day but fail to invest in their marriage or relationship, but relationships take much more than love to be successful.</p>
    <p>This innovative one-day seminar helps couples to breathe new life into their relationship</p>
  </div>

  <section class="gains">
    <h3 class="gains-heading">What you will gain from<br>Declan’s seminar:</h3>
    <ul class="gains-list">
      <li><svg viewBox="0 0 13 13"><path d="M1 7 L5 11 L12 1" fill="none" stroke="#1b8fd9" stroke-width="1.8"/></svg>How to turn an argument into a moment of closeness – Easier than you think!</li>
      <li><svg viewBox="0 0 13 13"><path d="M1 7 L5 11 L12 1" fill="none" stroke="#1b8fd9" stroke-width="1.8"/></svg>Know what stress is doing to your relating and the two skillsets will make a big difference to each other’s stress-load.</li>
      <li><svg viewBox="0 0 13 13"><path d="M1 7 L5 11 L12 1" fill="none" stroke="#1b8fd9" stroke-width="1.8"/></svg>The role of pleasure in an emotionally-committed relationship and that’s more than sex!</li>
      <li><svg viewBox="0 0 13 13"><path d="M1 7 L5 11 L12 1" fill="none" stroke="#1b8fd9" stroke-width="1.8"/></svg>Identify the traps of committed relationships – and why being in a relationship doesn’t have to be a struggle.</li>
      <li><svg viewBox="0 0 13 13"><path d="M1 7 L5 11 L12 1" fill="none" stroke="#1b8fd9" stroke-width="1.8"/></svg>Learn how it’s not you or your partner’s fault - Identify the missing ingredients in your relationship and what you can do to get these back.</li>
      <li><svg viewBox="0 0 13 13"><path d="M1 7 L5 11 L12 1" fill="none" stroke="#1b8fd9" stroke-width="1.8"/></svg>What the research says about the ingredients of great sex</li>
      <li><svg viewBox="0 0 13 13"><path d="M1 7 L5 11 L12 1" fill="none" stroke="#1b8fd9" stroke-width="1.8"/></svg>What to do about the three drains on your relationship: boredom, having nothing to say and those same-old arguments.</li>
      <li><svg viewBox="0 0 13 13"><path d="M1 7 L5 11 L12 1" fill="none" stroke="#1b8fd9" stroke-width="1.8"/></svg>You will also practice using Declan’s negotiation tool that he developed for couples as well. Declan’s seminars are fun, informative and practical.</li>
    </ul>
  </section>

  <section class="presenter-band">
    <div class="presenter-photo" role="img" aria-label="Portrait of the presenter outdoors in front of green foliage"></div>
    <div class="presenter-text">
      <h3 class="presenter-heading">ABOUT THE PRESENTER:</h3>
      <p>Declan Marlowe is a highly skilled couples therapist and educator, who is known for his innovative and creative approaches in his work. He has appeared on Harbourline TV’s Morning Lounge show and Bayview Network’s The Roundtable as well as being interviewed on radio and in print.</p>
      <p>Declan’s seminars are run along brain-based education principles that he learnt from Dr Alan Whitford’s training in the USA, so that you will remember your new learning and integrate it into your life.</p>
      <p class="booking">Take your relationship to the next level and book your seat now:
        <span class="booking-url">http://www.declanmarlowe.com.au/couples.html</span></p>
    </div>
  </section>
</div>
</body>
</html>
```